BrimKeel Limited needs a business card design

We need a business card design that reflects both professionalism and innovation and captures our brand identity. We provide online enterprise solutions to HR and executive management. We would like to use the colors in our logo (Blue and Orange). See attached file.

We would like a more creative design than the existing attached business card but maintain the same information on it.

To see our products site, please visit www.brimkeel.example which reflects more our identity
Updates

Please see our site: www.brimkeel.example, not www.brimkeel.example.co.uk for our colors and look and feel

Target Market(s)

Senior Executives

Industry/Entity Type

Business

Requirements
Must have
• Logo and use of logo colors
Nice to have
• Icons
Should not have
• Images

```html
<!DOCTYPE html>
<html lang="en">
<head>
<meta charset="utf-8">
<title>BrimKeel Limited – Business Card</title>
<link rel="stylesheet" href="https://fonts.googleapis.com/css2?family=Open+Sans:wght@400;600;800&display=swap">
<style>
  :root {
    --brand-blue: #1d5c99;
    --brand-blue-dark: #174b7e;
    --brand-orange: #f39200;
    --card-white: #ffffff;
    --page-bg: #e9ecef;
    --text-light: #dbe7f3;
  }
  * { box-sizing: border-box; margin: 0; padding: 0; }
  html, body { width: 900px; height: 1200px; overflow: hidden; }
  body {
    background: var(--page-bg);
    font-family: "Open Sans", Arial, sans-serif;
    display: flex;
    align-items: center;
    justify-content: center;
    gap: 60px;
  }
  .card {
    width: 370px;
    height: 572px;
    position: relative;
    box-shadow: 0 10px 28px rgba(0,0,0,0.18);
    overflow: hidden;
  }

  /* Front */
  .card-front {
    background: var(--card-white);
    display: flex;
    flex-direction: column;
    align-items: center;
    justify-content: center;
    gap: 14px;
  }
  .brand-name {
    display: flex;
    align-items: center;
    gap: 10px;
    font-size: 34px;
    font-weight: 600;
    color: var(--brand-blue);
    line-height: 1;
  }
  .brand-square {
    width: 14px;
    height: 14px;
    background: var(--brand-orange);
    flex: none;
  }
  .front-company {
    font-size: 11px;
    font-weight: 600;
    letter-spacing: 2px;
    color: var(--brand-blue);
  }

  /* Back */
  .card-back {
    background: linear-gradient(160deg, var(--brand-blue) 0%, var(--brand-blue-dark) 100%);
    color: var(--card-white);
  }
  .name-bar {
    position: absolute;
    top: 64px;
    right: 0;
    width: 230px;
    background: var(--brand-orange);
    padding: 14px 20px;
  }
  .person-name {
    font-size: 18px;
    font-weight: 800;
    letter-spacing: 1px;
    text-transform: uppercase;
    white-space: nowrap;
  }
  .person-role {
    font-size: 10px;
    font-weight: 600;
    letter-spacing: 1.5px;
    text-transform: uppercase;
    margin-top: 2px;
  }
  .contact-block {
    position: absolute;
    top: 200px;
    right: 40px;
    text-align: right;
    font-size: 12.5px;
    line-height: 1.7;
    color: var(--text-light);
  }
  .contact-group + .contact-group { margin-top: 18px; }
  .social-row {
    position: absolute;
    left: 40px;
    bottom: 44px;
    display: flex;
    gap: 10px;
  }
  .social-tile {
    width: 26px;
    height: 26px;
    background: var(--text-light);
    border-radius: 3px;
  }
  .back-web {
    position: absolute;
    right: 40px;
    bottom: 48px;
    font-size: 12px;
    font-weight: 600;
    color: var(--card-white);
  }
</style>
</head>
<body>
  <section class="card card-front" aria-label="Business card front">
    <div class="brand-name">
      <span class="brand-square"></span>
      <span>BrimKeel</span>
    </div>
    <div class="front-company">BRIMKEEL LIMITED</div>
  </section>

  <section class="card card-back" aria-label="Business card back">
    <div class="name-bar">
      <div class="person-name">Mara Lindqvist</div>
      <div class="person-role">Managing Director</div>
    </div>
    <div class="contact-block">
      <div class="contact-group">
        <div>14 Harbourline House</div>
        <div>Quay Street</div>
        <div>London EC2</div>
      </div>
      <div class="contact-group">
        <div>+1 555 010 2424 (US)</div>
        <div>+44 555 010 3636 (UK)</div>
      </div>
      <div class="contact-group">
        <div>mara@brimkeel.example</div>
      </div>
    </div>
    <div class="social-row" aria-label="Social links">
      <span class="social-tile"></span>
      <span class="social-tile"></span>
      <span class="social-tile"></span>
      <span class="social-tile"></span>
    </div>
    <div class="back-web">www.brimkeel.example</div>
  </section>
</body>
</html>
```